Flyer for annual KESTREL SUMMIT 2020

I would like a church event flyer designed. The event is called "KESTREL SUMMIT 2020". I am looking for a professional, yet catchy design that uses our brand colors and logo creatively while communicating key information of the event effectively.

1. The logo is attached in two color formats. The designer has the choice to use them as he/she want.

2. The location of the event is: Harlow Community Center, 239 Fennimore Street, Portland, ME 04117

3. Time and date of event. The designer can organize and format the date and time as he/she pleases.
Thursday December 31st @ 6:30PM
Friday January 1st @ 6:30PM
Saturday 2nd @ 6:30PM
Sunday 3rd @ 4:30PM

4. The topic of the event is "In Fire and On Fire". The designer is free to use this phrase as he/she pleases to create a good composition.

5. Speaker: Prophet Marcus Olunde (2 pictures of the speaker to choose from are attached)

6. Contact information: contact@brightmeadowfold.org - Telephone number: 207 583 2914

7. I would also like the following three words on the flyer. These words describe the focus of the event: FIRE, REVIVAL, PROPHETIC

Target Market(s)

Young adults

Font styles to use
Sans Serif

Requirements
Must have
• Logo, speaker's picture
Should not have
• cross image, church image

```html
<!DOCTYPE html>
<html lang="en">
<head>
<meta charset="utf-8">
<title>Kestrel Summit 2020 – Flyer</title>
<link rel="stylesheet" href="https://fonts.googleapis.com/css2?family=Bebas+Neue&display=swap">
<style>
  :root {
    --navy: #0c2a70;
    --orange: #ff7a0d;
    --orange-deep: #ff5a06;
    --white: #ffffff;
  }
  html, body { margin: 0; padding: 0; overflow: hidden; }
  body { width: 927px; height: 1200px; background: var(--navy); }
  .flyer {
    position: relative;
    width: 927px;
    height: 1200px;
    background: var(--navy);
    overflow: hidden;
    font-family: "Bebas Neue", "Oswald", sans-serif;
    color: var(--white);
  }
  .flyer__bands { position: absolute; inset: 0; }
  .brand {
    position: absolute;
    top: 96px;
    right: 52px;
    display: flex;
    align-items: center;
    gap: 10px;
  }
  .brand__dot {
    width: 18px; height: 18px;
    border-radius: 50%;
    background: var(--orange);
  }
  .brand__name { font-size: 58px; line-height: 1; letter-spacing: 3px; color: var(--white); }
  .speaker-photo {
    position: absolute;
    left: 41px; top: 241px;
    width: 415px; height: 727px;
    border-radius: 150px 150px 0 0;
    background: linear-gradient(180deg, #2b1a14 0%, #d8441c 32%, #e14a1d 70%, #b33612 100%);
  }
  .speaker {
    position: absolute;
    right: 55px;
    text-align: right;
  }
  .speaker__label { top: 428px; font-size: 22px; line-height: 1; }
  .speaker__name { top: 470px; font-size: 54px; line-height: 1; letter-spacing: 0.5px; }
  .schedule {
    position: absolute;
    right: 55px;
    top: 573px;
    margin: 0; padding: 0;
    list-style: none;
    text-align: right;
  }
  .schedule__item { font-size: 31px; line-height: 38.5px; white-space: nowrap; }
  .schedule__day { font-size: 18px; }
  .schedule__suffix { font-size: 18px; }
  .schedule__sep { padding: 0 8px; }
  .theme { position: absolute; right: 57px; text-align: right; line-height: 1; }
  .theme__focus { top: 880px; font-size: 54px; color: var(--navy); }
  .theme__title { top: 922px; font-size: 80px; color: var(--white); }
  .contact, .venue {
    position: absolute;
    top: 1070px;
    font-size: 27px;
    line-height: 33px;
    color: var(--orange);
  }
  .contact { left: 37px; }
  .venue { right: 62px; text-align: right; }
</style>
</head>
<body>
<main class="flyer">
  <svg class="flyer__bands" width="927" height="1200" viewBox="0 0 927 1200" aria-hidden="true">
    <defs>
      <linearGradient id="band-top" x1="0" y1="0" x2="1" y2="0">
        <stop offset="0" stop-color="var(--orange-deep)" style="stop-color:#ff5a06"/>
        <stop offset="1" stop-color="#ff8a10"/>
      </linearGradient>
      <linearGradient id="band-bottom" x1="0" y1="0" x2="1" y2="0">
        <stop offset="0" stop-color="#ff8a10"/>
        <stop offset="1" stop-color="#ff5a06"/>
      </linearGradient>
    </defs>
    <polygon points="0,71 923,328 0,612" fill="url(#band-top)"/>
    <polygon points="0,988 927,719 927,1010 0,1027" fill="url(#band-bottom)"/>
  </svg>

  <div class="brand">
    <span class="brand__dot"></span>
    <span class="brand__name">HALVEN</span>
  </div>

  <div class="speaker-photo" role="img" aria-label="Portrait of speaker Prophet Marcus Olunde in an orange suit"></div>

  <p class="speaker speaker__label" style="margin:0">SPEAKER</p>
  <h1 class="speaker speaker__name" style="margin:0;font-weight:400">PROPHET MARCUS OLUNDE</h1>

  <ul class="schedule">
    <li class="schedule__item"><span class="schedule__day">THURSDAY</span> DECEMBER 31<span class="schedule__suffix">ST</span><span class="schedule__sep">|</span>6:30PM</li>
    <li class="schedule__item"><span class="schedule__day">FRIDAY</span> JANUARY 1<span class="schedule__suffix">ST</span><span class="schedule__sep">|</span>6:30PM</li>
    <li class="schedule__item"><span class="schedule__day">SATURDAY</span> JANUARY 2<span class="schedule__suffix">ND</span><span class="schedule__sep">|</span>6:30PM</li>
    <li class="schedule__item"><span class="schedule__day">SUNDAY</span> JANUARY 3<span class="schedule__suffix">RD</span><span class="schedule__sep">|</span>4:30PM</li>
  </ul>

  <p class="theme theme__focus" style="margin:0">FIRE, REVIVAL, PROPHETIC</p>
  <h2 class="theme theme__title" style="margin:0;font-weight:400">IN FIRE AND ON FIRE</h2>

  <address class="contact" style="font-style:normal">
    CONTACT INFORMATION<br>
    CONTACT@BRIGHTMEADOWFOLD.ORG<br>
    TELEPHONE NUMBER: 207 583 2914
  </address>

  <address class="venue" style="font-style:normal">
    HARLOW COMMUNITY CENTER<br>
    239 FENNIMORE STREET<br>
    PORTLAND, ME 04117
  </address>
</main>
</body>
</html>
```